Harbor fairly.com a website to help those harmed by lending institutions

I am looking for a basic one page website that will be used to collect data from people filling out a form.
I will need certain key words to be optimized in order for the page to show up as high as possible in the search engines.

This web page is for people that have been harmed by their. Bank or lending institution due to inappropriate accounting practices or worse purposeful neglect.

Imagery should include an elderly person on the phone in distress because of over due bills.

Images of late notices
Images of threats of foreclosure.

** This site is to help people that are being unfairly treated even though they have made all their payments on time and the bank is commiting gross negligence.***

Some basic notes to start:

The color scheme should be similar to this site:

https://www.lendwatchry.com/

Here are some basic notes.

There will be more to follow.

There will need to be a collection form that people can link to and share their story.

Have you or someone you loved been hurt by their financial lending institution?

Have they/ you made all your payments on time only to constantly receive late notice penalties and additional accrued interest ?
Has your credit and good name been tarnished because your banks negligent or purposeful mis-handling of your account has caused the credit bureaus to drop your credit score?
Do you spend hours each month calling your bank to have them clear up their accounting mistakes?
Have you received threatening foreclosure notices even though you've made every payment on time ?

Well if so, you are not alone! This practise or gross incompetence is happening to many others just like you.

Your mortgage, student loan out other debt may have been sold to a new company that simply keeps losing the payments and you have to constantly clear you their errors on your time over and over again.

Budget is flexible based on design.

```html
<!DOCTYPE html>
<html lang="en">
<head>
<meta charset="utf-8">
<title>Harbor fairly.com — Help for people harmed by lending institutions</title>
<link href="https://fonts.googleapis.com/css2?family=Poppins:wght@300;400;500;600&display=swap" rel="stylesheet">
<style>
  :root{
    --ink:#111;
    --night:#0c0a10;
    --white:#fff;
    --grey-text:#8a8a8a;
    --line:#d9d9d9;
    --green:#0b9470;
    --green-soft:#3fae8e;
    --green-frame:#47b89a;
    --footer:#0c9168;
  }
  *{box-sizing:border-box;margin:0;padding:0}
  html,body{width:1200px;height:2302px;overflow:hidden}
  body{position:relative;font-family:'Poppins',sans-serif;color:var(--ink);background:var(--white)}

  /* hero */
  .hero{position:absolute;left:0;top:0;width:1200px;height:599px;background:var(--night);overflow:hidden}
  .hero-photo{position:absolute;left:445px;top:0;width:755px;height:599px;
    background:radial-gradient(ellipse at 60% 35%,#b9a596 0%,#6f5f56 35%,#2a2326 70%,var(--night) 100%)}
  .brand{position:absolute;left:80px;top:28px;display:flex;align-items:center;gap:8px;
    color:var(--green);font-weight:600;font-size:23px;letter-spacing:-.2px}
  .brand-dot{width:14px;height:14px;background:var(--green)}
  .hero-title{position:absolute;left:80px;top:205px;width:540px;color:var(--white);
    font-weight:500;font-size:34px;line-height:40px}
  .hero-sub{position:absolute;left:80px;top:343px;width:420px;color:var(--white);
    font-weight:300;font-size:16.5px;line-height:23px}
  .btn-outline{position:absolute;left:80px;top:426px;width:145px;height:38px;border:1.5px solid var(--white);
    color:var(--white);font-size:12.5px;font-weight:500;display:flex;align-items:center;justify-content:center}

  /* questions */
  .questions{position:absolute;left:0;top:599px;width:1200px;height:701px}
  .photo-frame{position:absolute;left:200px;top:81px;width:320px;height:498px;border:1.5px solid var(--green-frame)}
  .photo-card{position:absolute;left:239px;top:121px;width:320px;height:498px;
    background:linear-gradient(160deg,#e8e4de 0%,#c9bdb4 40%,#7a2c3a 70%,#4a3a33 100%);
    box-shadow:0 18px 40px rgba(0,0,0,.12)}
  .question-list{position:absolute;left:636px;top:156px;width:364px;list-style:none}
  .question-list li{position:relative;padding-left:44px;color:var(--grey-text);font-size:16px;
    line-height:24px;text-align:justify;margin-bottom:23px}
  .question-list svg{position:absolute;left:2px;top:3px}

  /* band */
  .band{position:absolute;left:0;top:1300px;width:1200px;height:238px;
    background:linear-gradient(90deg,#46ad8f 0%,#54b797 50%,#4aaf90 100%);text-align:center;color:var(--white)}
  .band-title{margin-top:83px;font-size:31px;font-weight:500}
  .band-sub{margin-top:2px;font-size:16.5px;font-weight:400}

  /* contact */
  .contact-title{position:absolute;left:0;top:1610px;width:1200px;text-align:center;font-size:25px;font-weight:500}
  .field{position:absolute;height:39px;border:1px solid var(--line);color:#9a9a9a;font-size:11.5px;
    padding:0 22px;display:flex;align-items:center}
  .field.message{align-items:flex-start;padding-top:12px}
  .btn-submit{position:absolute;left:520px;top:1943px;width:159px;height:39px;background:var(--green);
    color:var(--white);font-size:12.5px;font-weight:600;display:flex;align-items:center;justify-content:center}

  /* footer */
  .footer{position:absolute;left:0;top:2061px;width:1200px;height:241px;background:var(--footer);color:var(--white);
    font-size:11.5px;line-height:19px;font-weight:300}
  .copyright{position:absolute;left:80px;top:75px}
  .keywords{position:absolute;top:75px;list-style:none}
  .keywords li::before{content:"•";margin-right:8px}
  .kw-a{left:438px}.kw-b{left:798px}
  .social{position:absolute;left:1153px;top:79px;display:flex;flex-direction:column;gap:12px}
  .social span{width:13px;height:13px;background:var(--white);border-radius:2px}
</style>
</head>
<body>

<header class="hero">
  <div class="hero-photo" role="img" aria-label="Elderly man on the phone, holding his head in distress"></div>
  <div class="brand"><span class="brand-dot"></span>Harbor fairly.com</div>
  <h1 class="hero-title">Have been harmed by your Bank or Lending insti-tution</h1>
  <p class="hero-sub">due to inappropriate accounting practices or worse purposeful neglect?</p>
  <a class="btn-outline">Contact Now!</a>
</header>

<section class="questions">
  <div class="photo-frame"></div>
  <div class="photo-card" role="img" aria-label="Elderly man in a kitchen reading a late notice while holding a mug"></div>
  <ul class="question-list">
    <li><svg width="18" height="18" viewBox="0 0 18 18"><circle cx="9" cy="9" r="7.5" fill="none" stroke="#8a8a8a" stroke-width="1.3"/><path d="M5.5 9.2l2.5 2.4 5-5.2" fill="none" stroke="#8a8a8a" stroke-width="1.3"/></svg>Have they/ you made all your payments on time only to constantly receive late notice penalties and additional accrued interest?</li>
    <li><svg width="18" height="18" viewBox="0 0 18 18"><circle cx="9" cy="9" r="7.5" fill="none" stroke="#8a8a8a" stroke-width="1.3"/><path d="M5.5 9.2l2.5 2.4 5-5.2" fill="none" stroke="#8a8a8a" stroke-width="1.3"/></svg>Has your credit and good name been tarnished because your banks negligent or purposeful mis-handling of your ac-count has caused the credit bureaus to drop your credit score?</li>
    <li><svg width="18" height="18" viewBox="0 0 18 18"><circle cx="9" cy="9" r="7.5" fill="none" stroke="#8a8a8a" stroke-width="1.3"/><path d="M5.5 9.2l2.5 2.4 5-5.2" fill="none" stroke="#8a8a8a" stroke-width="1.3"/></svg>Do you spend hours each month calling your bank to have them clear up their accounting mistakes?</li>
    <li><svg width="18" height="18" viewBox="0 0 18 18"><circle cx="9" cy="9" r="7.5" fill="none" stroke="#8a8a8a" stroke-width="1.3"/><path d="M5.5 9.2l2.5 2.4 5-5.2" fill="none" stroke="#8a8a8a" stroke-width="1.3"/></svg>Have you received threatening foreclo-sure notices even though you've made every payment on time?</li>
  </ul>
</section>

<section class="band" role="img" aria-label="Smiling senior people under a green tint">
  <h2 class="band-title">Well if so, you are not alone!</h2>
  <p class="band-sub">This practise or gross incompetence is happening to many others just like you.</p>
</section>

<section class="contact">
  <h2 class="contact-title">Contact Us Today!</h2>
  <div class="field" style="left:200px;top:1677px;width:256px">Enter your Name</div>
  <div class="field" style="left:473px;top:1677px;width:254px">Email</div>
  <div class="field" style="left:744px;top:1677px;width:256px">Phone</div>
  <div class="field" style="left:200px;top:1733px;width:391px">Loan/Account Type</div>
  <div class="field" style="left:608px;top:1733px;width:392px">Name of Bank / Lending institution</div>
  <div class="field message" style="left:200px;top:1789px;width:800px;height:119px">Message ...</div>
  <a class="btn-submit">Submit</a>
</section>

<footer class="footer">
  <p class="copyright">© Copyright 2019 Harbor Fairly Group,<br>All rights reserved.</p>
  <ul class="keywords kw-a">
    <li>Constantly charged additional accrued interest</li>
    <li>Constantly receive late notice penalties</li>
    <li>Hurt by financial lending institution</li>
    <li>Banks negligent for your account</li>
  </ul>
  <ul class="keywords kw-b">
    <li>received threatening foreclosure notices</li>
    <li>Accounting mistakes of Banks</li>
    <li>Miss-handling of your account</li>
  </ul>
  <div class="social"><span></span><span></span></div>
</footer>

</body>
</html>
```